Portal Panel Medic need professional looking business card printed on plastic, Commericial, Industri

We are family owned and operated garage door company in Indianapolis, Indiana. We sale service and install dock equipment, doors, operators. We are looking to expand our commercial/ industrial division. We also service all residential doors and operators. We are looking for a business that stands out of the crowd. We are committed to have the best customer service in the industry.

Target Market(s)

National and local general contractors, National/ Corpate service accounts,

Industry/Entity Type

Business Service

Contact Information for Business Card

To be printed on plastic stock

Font styles to use
Sans Serif

Colors
ffffff
f04a50
ec1f27

Requirements
Must have
• Name, website,email, phone number, position.
Nice to have
• A standout professional design

```html
<!DOCTYPE html>
<html lang="en">
<head>
<meta charset="utf-8">
<title>Portal Panel Medic – Business Card</title>
<link rel="stylesheet" href="https://fonts.googleapis.com/css2?family=Lato:wght@300;400;700;900&display=swap">
<style>
  :root {
    --stage: #151515;
    --red: #ec1f27;
    --red-soft: #f04a50;
    --white: #ffffff;
    --ink: #555555;
    --ink-light: #6a6a6a;
  }
  * { margin: 0; padding: 0; box-sizing: border-box; }
  html, body {
    width: 1200px; height: 456px; overflow: hidden;
    background: var(--stage);
    font-family: "Lato", sans-serif;
  }
  .canvas { position: relative; width: 1200px; height: 456px; }

  .card { position: absolute; top: 67px; width: 532px; height: 320px; }

  /* Front */
  .card-front { left: 45px; background: var(--red); }
  .front-brand {
    position: absolute; left: 0; right: 0; top: 160px;
    display: flex; align-items: center; justify-content: center; gap: 10px;
  }
  .brand-square { width: 14px; height: 14px; background: var(--white); }
  .front-brand .brand-name {
    color: var(--white); font-weight: 900; font-size: 30px;
    text-transform: uppercase; letter-spacing: 0.5px; line-height: 1;
  }
  .front-phone {
    position: absolute; left: 0; right: 0; top: 204px; text-align: center;
    color: var(--white); font-size: 21px; font-weight: 400; letter-spacing: 0.5px;
  }

  /* Back */
  .card-back { left: 616px; background: var(--white); }
  .brand-tab {
    position: absolute; left: 53px; top: 0; width: 116px; height: 135px;
    background: var(--red); border-radius: 0 0 6px 6px;
    display: flex; flex-direction: column; align-items: center; justify-content: center;
    padding: 0 8px; text-align: center;
  }
  .brand-tab .brand-name {
    color: var(--white); font-weight: 900; font-size: 15px;
    text-transform: uppercase; line-height: 1.1;
  }
  .brand-tab .tab-phone {
    margin-top: 10px; color: var(--white); font-size: 9px; font-weight: 400;
  }
  .person {
    position: absolute; left: 53px; top: 199px; width: 428px;
    display: flex; justify-content: space-between; align-items: baseline;
  }
  .person-name { font-size: 30px; font-weight: 300; color: var(--ink-light); letter-spacing: 0.5px; }
  .person-name .surname { color: var(--red); font-weight: 400; }
  .person-role { font-size: 10px; font-weight: 700; color: var(--red); letter-spacing: 0.3px; }
  .rule { position: absolute; left: 53px; top: 231px; width: 428px; height: 5px; background: var(--red); }
  .contact {
    position: absolute; left: 53px; top: 243px; width: 440px;
    font-size: 10.5px; line-height: 15px; color: var(--ink);
  }
  .contact .label { color: var(--red); font-weight: 700; }
  .contact .item { margin-right: 5px; }
</style>
</head>
<body>
<div class="canvas">
  <section class="card card-front">
    <div class="front-brand">
      <span class="brand-square"></span>
      <span class="brand-name">Portal Panel Medic</span>
    </div>
    <p class="front-phone">(317) 555-0142</p>
  </section>

  <section class="card card-back">
    <div class="brand-tab">
      <span class="brand-name">Portal Panel Medic</span>
      <span class="tab-phone">(317) 555-0142</span>
    </div>
    <div class="person">
      <h1 class="person-name">JOHN <span class="surname">DOE</span></h1>
      <span class="person-role">PANEL MEDIC</span>
    </div>
    <div class="rule"></div>
    <div class="contact">
      <p><span class="label">Address:</span> 482 Harbor Lane Indianapolis, IN 46201</p>
      <p>
        <span class="item"><span class="label">Phone:</span> 000 . 1234 .5678</span>
        <span class="item"><span class="label">Email:</span> admin@portalpanel.com</span>
        <span class="item"><span class="label">Website:</span> www.portalpanel.com</span>
      </p>
    </div>
  </section>
</div>
</body>
</html>
```